Webdesign für Onlineshop
Zielgruppe
Wir verkaufen in unserem Onlineshop alles zum Thema Wohnen mit dem Schwerpunkt Möbel. Die Hauptzielgruppe ist zwischen 25 und 45 Jahren.
Aufgabenstellung
Wir bevorzugen ein modernes, flaches und aufgeräumtes Design ähnlich wie velm.de / dorano88.de mit dem Fokus auf Preisaggressivität und Rabatte.
- Das Grundlayout muss so bleiben, wie es aktuell ist. Natürlich dürfen einzelne Elemente verschoben / versetzt werden.
- Im Header sollte Platz für eine kleine Werbefläche sein (ähnlich wie der konfigurierbare Kleiderschrank).
- Der Shop basiert auf Magento 1.9.
- Die Rabatte in den Produktdetailseiten müssen genauso aufgebaut sein
- Die Suche sollte in den Header platziert werden und nicht im Menü
- Ein SSL Logo soll im Header platziert weden
- Die Vorteile (Kostenloser Versand, Sicher einkaufen, Kauf auf Rechnung) sollen im Header erscheinen
- Das Design sollte responsive sein
Es wird nur das reine Design ohne Programmierung benötigt.

```html
<!DOCTYPE html>
<html lang="de">
<head>
<meta charset="utf-8">
<title>Quellmark3berg – Funktionssofa grün-weiß</title>
<link href="https://fonts.googleapis.com/css2?family=Raleway:wght@400;500;600;700&display=swap" rel="stylesheet">
<style>
:root{
  --green:#84ab3c;
  --green-dark:#6f9430;
  --text:#444;
  --muted:#888;
  --line:#e2e2e2;
  --topbar:#f0f0f0;
  --red:#e0463c;
  --footer:#3b3b3b;
  --footer-bottom:#2b2b2b;
  --white:#fff;
}
*{box-sizing:border-box;margin:0;padding:0}
html,body{width:1073px;height:1200px;overflow:hidden;background:var(--white)}
body{position:relative;font-family:"Raleway",sans-serif;color:var(--text)}
.abs{position:absolute}
a{color:inherit;text-decoration:none}

/* top bar */
.topbar{left:0;top:0;width:1073px;height:25px;background:var(--topbar);font-size:6.5px;color:#666}
.topbar .item{position:absolute;display:flex;align-items:center;gap:5px;line-height:1.2}
.topbar .links{position:absolute;left:679px;top:8px;font-size:7.5px;color:var(--green)}
.topbar .links span{margin:0 6px;color:#bbb}
.topbar .account{position:absolute;left:794px;top:0;width:70px;height:25px;background:var(--green);color:#fff;display:flex;align-items:center;justify-content:space-around;font-size:6.5px}
.topbar .account div{display:flex;align-items:center;gap:4px}
.vsep{position:absolute;top:7px;width:1px;height:12px;background:#ddd}

/* header */
.brand{left:209px;top:38px;display:flex;align-items:center;gap:8px;font-size:15px;font-weight:600;color:#3a3a3a;letter-spacing:1.5px;text-transform:uppercase}
.brand i{display:block;width:14px;height:14px;background:var(--green)}
.search{left:433px;top:42px;width:262px;height:16px;border:1px solid var(--green);background:#fff}
.search svg{position:absolute;right:4px;top:2px}
.seal{width:19px;height:19px;border-radius:50%;background:#2e2e2e;border:2px solid #d9d9d9}
.seal.red{border-radius:3px;background:#d8343b;border:2px solid #eee;height:24px;width:17px}
.promo{left:772px;top:28px;width:92px;height:44px;background:#fff;overflow:hidden}
.promo .head{font-size:4.8px;font-weight:600;text-align:center;line-height:1.1;color:#333;text-transform:uppercase;white-space:nowrap}
.promo .pic{position:absolute;left:0;top:13px;width:92px;height:31px;background:linear-gradient(90deg,#cfcac3,#e8e4de 40%,#a89b8a 70%,#d8d3cc)}
.promo .tag{position:absolute;left:0;bottom:0;height:9px;width:92px;background:#c5222a;color:#fff;font-size:5.5px;font-weight:700;padding-left:24px;line-height:9px}
.promo .pct{position:absolute;left:0;bottom:0;width:23px;height:16px;background:#f5c400;color:#c5222a;font-weight:700;font-size:11px;text-align:center;line-height:16px}

.nav{left:209px;top:74px;width:655px;height:38px;border-top:1px solid var(--line);display:flex;justify-content:space-between;align-items:center;font-size:8.5px;color:var(--green);font-weight:500}

/* product stage */
.stage{left:0;top:112px;width:489px;height:379px;background:var(--green)}
.wish{left:209px;top:133px;width:135px;height:1px;background:rgba(255,255,255,.55)}
.wish-label{left:356px;top:127px;font-size:8px;color:#fff;display:flex;align-items:center;gap:10px}
.photo{background:linear-gradient(160deg,#e9ece3 0%,#f4f4f1 35%,#b4c94b 50%,#9fbb33 62%,#d9d9d7 78%,#2f2f30 100%)}
.main-photo{left:210px;top:156px;width:319px;height:210px;box-shadow:-4px 5px 8px rgba(0,0,0,.25);z-index:2}
.thumb{top:385px;height:63px;width:96px}
.thumbs-track{left:209px;top:457px;width:271px;height:1px;background:rgba(255,255,255,.6)}
.thumbs-knob{left:233px;top:455px;width:62px;height:3px;background:#fff;border-radius:2px}
.stage-divider{left:493px;top:112px;width:1px;height:378px;background:#333;z-index:1}
.rail{left:879px;top:127px;width:2px;height:126px;background:#e8e8e8}
.rail-right{left:880px;top:112px;width:1px;height:382px;background:#f0f0f0}

/* product info */
.sku{left:545px;top:118px;font-size:6px;color:#aaa}
.title{left:544px;top:127px;font-size:20px;font-weight:500;color:var(--green);letter-spacing:.2px}
.desc{left:545px;top:156px;width:320px;font-size:9.5px;line-height:13.5px;color:#444}
.prices{left:545px;top:201px;width:319px;height:113px;background:#efefef;font-size:7.5px}
.prices .row{position:absolute;left:19px;right:20px;display:flex;justify-content:space-between}
.prices .neg{color:var(--red)}
.prices .old{text-decoration:line-through;color:#555}
.current{left:545px;top:291px;width:319px;height:23px;border:1.5px solid var(--green);background:#fff;display:flex;justify-content:space-between;align-items:center;padding:0 19px;font-size:8.5px;font-weight:700;color:#222}
.current b{color:var(--green);font-size:9.5px}
.qty{left:545px;top:358px;width:94px;height:33px;border:1.5px solid var(--green);display:flex;align-items:center;font-size:10px}
.qty .ctl{width:47px;display:flex;justify-content:space-around;color:var(--green);align-items:center}
.qty .ctl b{color:#333;font-weight:500;font-size:11px}
.qty .unit{flex:1;height:100%;border-left:1.5px solid var(--green);display:flex;align-items:center;justify-content:center;font-size:7.5px;color:#888}
.option{left:657px;display:flex;align-items:center;gap:8px;font-size:7.5px;color:#666;letter-spacing:.2px}
.option i{display:block;width:10px;height:10px;border:1.5px solid var(--green)}
.cart-btn{left:545px;top:413px;width:319px;height:33px;background:var(--green);color:#fff;font-size:10px;font-weight:500;display:flex;align-items:center;justify-content:center;letter-spacing:.2px}
.info-end{left:545px;top:490px;width:319px;height:1px;background:var(--line)}

/* sections */
.section-title{font-size:21px;color:var(--green);font-weight:500;letter-spacing:.2px}
.card-photo{top:559px;width:207px;height:136px}
.card-name{top:699px;width:207px;font-size:10px;line-height:14px;color:#444}
.card-price{top:737px;font-size:10px;font-weight:600;color:var(--green)}
.card-price s{color:#666;font-weight:400;font-size:8px;margin-right:4px}
.badge{background:var(--green);color:#fff;font-size:9px;padding:3px 8px}
.slider-line{left:209px;top:774px;width:651px;height:1px;background:var(--line)}
.slider-knob{left:321px;top:773px;width:124px;height:2px;background:#ccc}

.mini-photo{width:96px;height:63px}
.mini-name{font-size:7.5px;line-height:10px;color:#555;width:100px}
.mini-price{font-size:9.5px;font-weight:600;color:var(--green)}
.mini-price s{font-size:7.5px;color:#666;font-weight:400;margin-right:4px}
.mini-price span.plain{font-size:7.5px;color:#666;font-weight:400;margin-right:4px}

.voucher{left:656px;top:864px;width:207px;height:149px;background:linear-gradient(135deg,#8cb243,#7aa233)}
.voucher .frame{position:absolute;inset:3px;border:1.5px solid rgba(255,255,255,.8)}
.voucher h3{position:absolute;top:18px;width:100%;text-align:center;color:#fff;font-size:18px;font-weight:700}
.voucher p{position:absolute;top:59px;left:26px;right:26px;text-align:center;color:#fff;font-size:6.8px;font-weight:600;line-height:10px}
.voucher .mail{position:absolute;left:22px;top:103px;width:163px;height:23px;background:#fff;font-size:7px;color:#777;padding-left:9px;line-height:23px}
.voucher .mail svg{position:absolute;right:9px;top:7px}

/* footer */
.footer{left:0;top:1060px;width:1073px;height:116px;background:var(--footer)}
.foot-head{top:1081px;font-size:8.5px;color:#fff;font-weight:500}
.foot-rule{top:1096px;height:1px;background:#666}
.foot-links{top:1104px;font-size:8px;line-height:13.5px;color:#9a9a9a}
.cert{top:1107px;width:33px;height:33px;border-radius:50%;background:#c9a43a;border:3px solid #e8e8e8}
.pay{width:30px;height:14px;background:#fff;border-radius:2px;font-size:5px;font-weight:700;color:#444;display:flex;align-items:center;justify-content:center;text-align:center;line-height:1;overflow:hidden}
.bottom{left:0;top:1176px;width:1073px;height:24px;background:var(--footer-bottom);font-size:6.5px;color:#ddd}
</style>
</head>
<body>

<!-- top bar -->
<div class="abs topbar">
  <div class="item" style="left:210px;top:8px">
    <svg width="8" height="8" viewBox="0 0 10 10"><path d="M2 1l2 2-1 1.5c.8 1.4 1.6 2.2 3 3L7.5 6l2 2-1.5 1.5C5 9 1 5 .5 1.5z" fill="#aaa"/></svg>
    0489 / 27 61 30 55</div>
  <div class="item" style="left:295px;top:8px">
    <svg width="9" height="9" viewBox="0 0 10 10"><rect x="1" y="2" width="8" height="7" fill="none" stroke="#aaa"/><path d="M1 4h8" stroke="#aaa"/></svg>
    Mo-Fr 9-21 Uhr Sa 10-15 Uhr</div>
  <div class="vsep" style="left:410px"></div>
  <div class="item" style="left:426px;top:6px">
    <svg width="14" height="9" viewBox="0 0 14 9"><rect x="0" y="1" width="8" height="6" fill="#aaa"/><path d="M8 3h3l2 2v2H8z" fill="#aaa"/><circle cx="3" cy="8" r="1" fill="#aaa"/><circle cx="11" cy="8" r="1" fill="#aaa"/></svg>
    <span style="margin-left:4px">Versandkostenfrei<br>alle Artikel im Online-Shop</span></div>
  <div class="item" style="left:559px;top:6px">
    <svg width="11" height="11" viewBox="0 0 10 10"><circle cx="5" cy="5" r="5" fill="#bbb"/><path d="M3 5l1.5 1.5L7 4" stroke="#fff" fill="none"/></svg>
    <span style="margin-left:2px">0% Finanzierung<br>+ weitere Zahlweisen</span></div>
  <div class="vsep" style="left:662px"></div>
  <div class="links">Zahlungsarten<span>|</span>Lieferung</div>
  <div class="account">
    <div><svg width="9" height="8" viewBox="0 0 10 9"><path d="M5 8.5L1 4.5A2.2 2.2 0 0 1 5 1.7 2.2 2.2 0 0 1 9 4.5z" fill="none" stroke="#fff" stroke-width="1.2"/></svg>15</div>
    <div><svg width="10" height="8" viewBox="0 0 11 9"><path d="M0 1h2l1.5 5h6L11 2.5H3" fill="none" stroke="#fff"/><circle cx="4" cy="8" r=".8" fill="#fff"/><circle cx="9" cy="8" r=".8" fill="#fff"/></svg>2</div>
  </div>
</div>

<!-- header -->
<div class="abs brand"><i></i>Quellmark3berg</div>
<div class="abs search">
  <svg width="11" height="11" viewBox="0 0 11 11"><circle cx="4.5" cy="4.5" r="3.5" fill="none" stroke="#555"/><path d="M7 7l3.5 3.5" stroke="#555"/></svg>
</div>
<div class="abs seal" style="left:709px;top:40px"></div>
<div class="abs seal red" style="left:740px;top:37px"></div>
<div class="abs promo">
  <div class="head">Kleiderschrank jetzt auch<br>selbst zusammenstellen</div>
  <div class="pic" role="img" aria-label="Foto eines Kleiderschranks mit Schiebetüren"></div>
  <div class="tag">EINFÜHRUNGSRABATT</div>
  <div class="pct">10%</div>
</div>

<nav class="abs nav">
  <a>WOHNEN</a><a>SCHLAFEN</a><a>KINDER-BABY</a><a>ESSEN</a><a>KÜCHE</a><a>BIS60%RABATT</a><a>SONSTIGES</a><a>SALE</a>
</nav>

<!-- product stage -->
<div class="abs stage"></div>
<div class="abs wish"></div>
<div class="abs wish-label">Artikel auf die Merkliste
  <svg width="12" height="11" viewBox="0 0 10 9"><path d="M5 8.5L1 4.5A2.2 2.2 0 0 1 5 1.7 2.2 2.2 0 0 1 9 4.5z" fill="none" stroke="#fff" stroke-width="1"/></svg>
</div>
<div class="abs stage-divider"></div>
<div class="abs photo main-photo" role="img" aria-label="Funktionssofa in Grün-Weiß mit Rückenkissen in hellem Wohnraum"></div>
<div class="abs photo thumb" style="left:209px" role="img" aria-label="Funktionssofa Ansicht von vorne"></div>
<div class="abs photo thumb" style="left:321px" role="img" aria-label="Funktionssofa als Bett ausgeklappt"></div>
<div class="abs photo thumb" style="left:433px;width:56px" role="img" aria-label="Funktionssofa Seitenansicht"></div>
<div class="abs thumbs-track"></div>
<div class="abs thumbs-knob"></div>
<div class="abs rail-right"></div>
<div class="abs rail"></div>

<!-- product info -->
<div class="abs sku">Artikel-Nr.: 19059</div>
<h1 class="abs title">FUNKTIONSSOFA GRÜN-WEIß</h1>
<p class="abs desc">inkl. 2 großer Rückenkissen, Bettkasten und Polyätherschaumpolsterung, Maße: B/H/T ca. 200/69-87/96 cm</p>
<div class="abs prices">
  <div class="row" style="top:9px"><span>Preis</span><span class="old">469,00 €**</span></div>
  <div class="row" style="top:31px"><span>23%Online-Rabatt von uns</span><span class="neg">-110,00 €**</span></div>
  <div class="row" style="top:53px"><span>10% Herbst-Sale</span><span class="neg">-35,90 €**</span></div>
  <div class="row" style="top:75px;align-items:center"><span>Unser Preis</span><span style="font-size:9.5px;margin-right:3px">323,10 €**</span></div>
</div>
<div class="abs current"><span>Aktueller Preis:</span><b>804,00 €**</b></div>

<div class="abs qty">
  <div class="ctl"><span>-</span><b>2</b><span>+</span></div>
  <div class="unit">STÜCK</div>
</div>
<div class="abs option" style="top:360px"><i></i>AUFBAU-/MONTAGE-SERVICE +79,00 €</div>
<div class="abs option" style="top:379px"><i></i>ENTSORGUNG IHRER ALTGARNITUR +79,00 €</div>
<div class="abs cart-btn">IN DEN WARENKORB LEGEN</div>
<div class="abs info-end"></div>

<!-- similar -->
<h2 class="abs section-title" style="left:209px;top:515px">ÄHNLICHE ARTIKEL</h2>

<div class="abs photo card-photo" style="left:209px;background:linear-gradient(170deg,#e8e6e2 0%,#f2f2f0 40%,#b6c84a 55%,#e9e9e9 72%,#5a3e2c 100%)" role="img" aria-label="Grün-weißes Funktionssofa vor Ziegelwand"></div>
<div class="abs card-name" style="left:209px;top:697px">Funktionssofa grün-weiß</div>
<div class="abs card-price" style="left:209px">804,00 €</div>

<div class="abs photo card-photo" style="left:433px;background:linear-gradient(170deg,#efe8dc 0%,#f4f1ec 40%,#4a4a4a 55%,#ececec 75%,#d9d3c8 100%)" role="img" aria-label="Schlafsofa in Weiß und Schwarzgrau"></div>
<div class="abs badge" style="left:425px;top:569px">-30%</div>
<div class="abs card-name" style="left:433px">Doppelschlafsofa in Kunstleder weiß und Stoff schwarz-grau</div>
<div class="abs card-price" style="left:432px"><s>520,00 €</s>334,00 €*</div>

<div class="abs photo card-photo" style="left:656px;background:linear-gradient(170deg,#e4e1d8 0%,#f0efea 40%,#3a3a3a 55%,#4a4a4a 70%,#b3afa7 100%)" role="img" aria-label="Dunkelgraues Schlafsofa im Loft"></div>
<div class="abs card-name" style="left:656px">Dauerschläfer, Dauerschlafsofa in dunkelgrau</div>
<div class="abs card-price" style="left:656px">368,00 €</div>

<div class="abs slider-line"></div>
<div class="abs slider-knob"></div>

<!-- popular -->
<h2 class="abs section-title" style="left:209px;top:819px">BELIEBTE ARTIKEL</h2>

<div class="abs photo mini-photo" style="left:209px;top:864px;background:linear-gradient(170deg,#e5e3df,#b6c84a 55%,#e6e6e6)" role="img" aria-label="Grün-weißes Sofa"></div>
<div class="abs mini-name" style="left:312px;top:868px">Funktionssofa grün-weiß</div>
<div class="abs mini-price" style="left:312px;top:914px">804,00 €</div>

<div class="abs photo mini-photo" style="left:433px;top:864px;background:linear-gradient(170deg,#efe8dc,#4a4a4a 55%,#ececec)" role="img" aria-label="Schwarz-weißes Schlafsofa"></div>
<div class="abs badge" style="left:427px;top:871px;font-size:7.5px;padding:2px 6px">-30%</div>
<div class="abs mini-name" style="left:537px;top:868px">Doppelschlafsofa in Kunstleder weiß und Stoff schwarz-grau</div>
<div class="abs mini-price" style="left:536px;top:914px"><s>520,00 €</s>334,00 €*</div>

<div class="abs" style="left:209px;top:939px;width:430px;height:1px;background:var(--line)"></div>
<div class="abs" style="left:424px;top:864px;width:1px;height:152px;background:var(--line)"></div>

<div class="abs photo mini-photo" style="left:209px;top:950px;background:linear-gradient(170deg,#d8d3cb,#8a7d70 55%,#4a3a30)" role="img" aria-label="Graue Ecksofa-Wohnlandschaft"></div>
<div class="abs mini-name" style="left:312px;top:954px">Funktionssofa grün-weiß</div>
<div class="abs mini-price" style="left:312px;top:1000px">804,00 €</div>

<div class="abs photo mini-photo" style="left:433px;top:950px;background:linear-gradient(170deg,#a5a29d,#c8302a 55%,#6b6560)" role="img" aria-label="Rotes Kunstledersofa"></div>
<div class="abs mini-name" style="left:537px;top:954px">Doppelschlafsofa in Kunstleder weiß und Stoff schwarz-grau</div>
<div class="abs mini-price" style="left:536px;top:1000px"><span class="plain">520,00 €</span>334,00 €*</div>

<div class="abs voucher">
  <div class="frame"></div>
  <h3>5 € GUTSCHEIN</h3>
  <p>Kostenlosen Newsletter abonnieren, von zahlreichen Aktionen profitieren und zusätzlich 5€ Gutschein sichern!</p>
  <div class="mail">E-mail
    <svg width="16" height="9" viewBox="0 0 16 9"><rect x="4" y="1" width="11" height="7" fill="none" stroke="var(--green)"/><path d="M4 1l5.5 4L15 1M0 3h3M1 5h2" stroke="var(--green)" fill="none"/></svg>
  </div>
</div>

<!-- footer -->
<footer class="abs footer"></footer>
<div class="abs foot-head" style="left:209px">ÜBER UNS</div>
<div class="abs foot-rule" style="left:209px;width:95px"></div>
<div class="abs foot-links" style="left:209px">Über uns<br>Kontakt<br>Impressum</div>

<div class="abs foot-head" style="left:321px">KUNDENSERVICE</div>
<div class="abs foot-rule" style="left:321px;width:206px"></div>
<div class="abs foot-links" style="left:321px">Zahlungsarten<br>Lieferung<br>AGB<br>Widerrufsrecht</div>
<div class="abs foot-links" style="left:433px">Datenschutz<br>Katalog<br>Blog</div>

<div class="abs foot-head" style="left:545px">ZERTIFIZIERT</div>
<div class="abs foot-rule" style="left:545px;width:150px"></div>
<div class="abs cert" style="left:545px"></div>
<div class="abs cert" style="left:602px;background:#2e2e2e"></div>
<div class="abs cert" style="left:660px;background:#d2a92c"></div>

<div class="abs foot-head" style="left:712px">ZAHLUNGSARTEN</div>
<div class="abs foot-rule" style="left:712px;width:151px"></div>
<div class="abs pay" style="left:712px;top:1106px;font-size:4.3px">Banküber-<br>weisung -3%</div>
<div class="abs pay" style="left:753px;top:1106px;color:#1f4a8a">Zahlfix</div>
<div class="abs pay" style="left:793px;top:1106px;color:#d6781c">Direktpay</div>
<div class="abs pay" style="left:833px;top:1106px;color:#1e5fa8">Rechnly</div>
<div class="abs pay" style="left:712px;top:1125px;font-size:3.8px">NACHNAHME</div>
<div class="abs pay" style="left:753px;top:1125px;color:#c5222a">Ringkarte</div>
<div class="abs pay" style="left:793px;top:1125px;color:#1a2b7a;font-size:6px">Karto</div>
<div class="abs pay" style="left:833px;top:1125px;font-size:3.3px">FINANZIERUNG</div>

<div class="abs bottom">
  <span class="abs" style="left:210px;top:9px">FOLLOW US</span>
  <span class="abs" style="left:262px;top:9px;color:#fff">Socialo</span>
  <span class="abs" style="left:747px;top:9px">Copyright © 2016. All Rights Reserved</span>
</div>

</body>
</html>
```